Upcoming Importing and Distribution Business Needs A Packaging Design!

We are an importing and distribution company that is importing reams of paper into New Zealand; now we have confirmed the product we need a design mocked up for the reams of paper!

We need packaging for the individual reams and then also the box that will hold 5 reams.

Each ream needs to have information on it, including:
A4 Size
500 sheets
80g/m2
Home and Office Use

(On the back of the product) Company contact information
Harrowgate Traders Limited
PO Box 4862
Christchurch 8356
New Zealand
(Email) office@harrowgatetraders.example.

It is being brought in by our company, Harrowgate Traders (logo attached)

We can't have too many colours in the design as it drives the price up very quickly.

Target Market(s)

Businesses and people that use paper to print documents

Industry/Entity Type

Retail

Requirements
Must have
• Clear simplistic labelling, be eye catching and stand out.
Should not have
• Not too many colours, will drive the price up too much

```html
<!DOCTYPE html>
<html lang="en">
<head>
<meta charset="utf-8">
<title>Harrowgate Traders – A4 Ream Wrapper</title>
<link href="https://fonts.googleapis.com/css2?family=Libre+Baskerville:wght@400;700&display=swap" rel="stylesheet">
<style>
  :root{
    --bg:#e9ebec;
    --paper:#ffffff;
    --red:#d42f2c;
    --orange:#fbb42a;
    --ink:#333333;
    --rule:#9a9a9a;
  }
  *{margin:0;padding:0;box-sizing:border-box}
  html,body{width:1200px;height:991px;overflow:hidden}
  body{background:var(--bg);font-family:"Libre Baskerville",Georgia,serif;color:var(--ink);position:relative}
  .wrapper{position:absolute;left:393px;top:35px;width:414px;height:920px}
  .panel{position:absolute;background:var(--paper);border:1px solid var(--rule);overflow:hidden}
  .top-flap{left:68px;top:0;width:277px;height:70px}
  .front{left:68px;top:70px;width:277px;height:389px}
  .side-left{left:0;top:70px;width:68px;height:389px}
  .side-right{left:345px;top:70px;width:69px;height:389px}
  .bottom-flap{left:68px;top:459px;width:277px;height:70px}
  .back{left:68px;top:529px;width:277px;height:391px}

  .brand{display:flex;align-items:center;gap:6px;font-weight:700;font-size:11px;color:var(--ink);white-space:nowrap}
  .brand-dot{width:16px;height:16px;border-radius:50%;border:2px solid var(--orange);flex:none}
  .tagline{font-weight:700;color:var(--red);font-size:9px}

  .top-flap .content{position:absolute;inset:0;display:flex;flex-direction:column;align-items:center;justify-content:center;gap:5px;transform:rotate(180deg)}
  .bottom-flap .content{position:absolute;inset:0;display:flex;flex-direction:column;align-items:center;justify-content:center;gap:5px}

  .front .brand{position:absolute;top:26px;left:50%;transform:translateX(-50%)}
  .use{position:absolute;top:168px;left:0;right:0;text-align:center;font-weight:700;color:var(--red);font-size:17px}
  .use-rule{position:absolute;top:194px;left:38px;right:38px;height:2px;background:var(--orange)}
  .size-mark{position:absolute;top:198px;left:104px;font-weight:700;color:var(--red);font-size:76px;line-height:1}
  .size-mark .num{position:absolute;left:42px;top:-4px;color:var(--orange);font-size:56px;font-weight:400}
  .band{position:absolute;left:0;right:0;top:284px;height:40px;background:var(--orange)}
  .spec{position:absolute;top:280px;left:96px;width:86px;border:1px solid var(--ink);background:var(--paper);text-align:center;font-weight:700;font-size:10px}
  .spec div{padding:3px 0}
  .spec div+div{border-top:1px solid var(--ink)}

  .side-text{position:absolute;top:210px;left:50%;width:160px;transform:translateX(-50%) rotate(-90deg);transform-origin:center;font-size:8px;font-weight:700;text-align:center;white-space:nowrap}
  .side-left .band,.side-right .band{}
  .side-mark{position:absolute;top:344px;left:50%;transform:translateX(-50%);width:22px;height:22px;border-radius:50%;border:2px solid var(--orange)}

  .back .band{top:95px;height:42px}
  .contact{position:absolute;top:88px;left:78px;width:121px;background:var(--paper);padding:6px 4px;font-size:6.5px;line-height:1.45;text-align:left}
  .back .brand{position:absolute;right:10px;bottom:14px;font-size:9px}
  .back .brand-dot{width:13px;height:13px}
</style>
</head>
<body>
  <div class="wrapper">
    <section class="panel top-flap">
      <div class="content">
        <div class="brand"><span class="brand-dot"></span>Harrowgate Traders</div>
        <div class="tagline">Home and Office Use</div>
      </div>
    </section>

    <section class="panel side-left">
      <div class="band"></div>
      <p class="side-text">A4 · 500 Sheets · 80g/m2</p>
      <span class="side-mark"></span>
    </section>

    <section class="panel front">
      <div class="brand"><span class="brand-dot"></span>Harrowgate Traders</div>
      <h1 class="use">Home and Office Use</h1>
      <div class="use-rule"></div>
      <div class="band"></div>
      <div class="size-mark">A<span class="num">4</span></div>
      <div class="spec">
        <div>80g/m2</div>
        <div>500 x A4</div>
      </div>
    </section>

    <section class="panel side-right">
      <div class="band"></div>
      <p class="side-text">A4 · 500 Sheets · 80g/m2</p>
      <span class="side-mark"></span>
    </section>

    <section class="panel bottom-flap">
      <div class="content">
        <div class="brand"><span class="brand-dot"></span>Harrowgate Traders</div>
        <div class="tagline">Home and Office Use</div>
      </div>
    </section>

    <section class="panel back">
      <div class="band"></div>
      <address class="contact" style="font-style:normal">
        Harrowgate Traders Limited<br>
        PO Box 4862<br>
        Christchurch 8356<br>
        New Zealand<br>
        office@harrowgatetraders.example
      </address>
      <div class="brand"><span class="brand-dot"></span>Harrowgate Traders</div>
    </section>
  </div>
</body>
</html>
```